Quarvine, Cosmetic skin care line

I am not looking to change my logo quarvine on the label just want someone to design a different label I want it to be very classy as it is already just want something different. My product target classier people and people with higher income and for woman and men but mostly women. Looking to keep the label background black

Target Market(s)

Classier and higer income women/men mostly women

Industry/Entity Type

Cosmetics

• I don't really know

Colors

Designer to choose colors to be used in the design.

Requirements
Must have
• It must keep the same quarvine logo and the same matte black background color
Nice to have
• I want a different layout and maybe different fonts for the label
Should not have

```html
<!DOCTYPE html>
<html lang="en">
<head>
<meta charset="utf-8">
<title>Quarvine Eye Corrector Serum Label</title>
<link rel="stylesheet" href="https://fonts.googleapis.com/css2?family=Saira+Condensed:wght@300;400&display=swap">
<style>
  :root {
    --label-black: #0e0f11;
    --ink-white: #ffffff;
    --accent-plum: #86338a;
  }
  html, body {
    margin: 0;
    padding: 0;
    width: 1200px;
    height: 1060px;
    overflow: hidden;
    background: var(--label-black);
  }
  .label {
    position: relative;
    width: 1200px;
    height: 1060px;
    background: var(--label-black);
    color: var(--ink-white);
    font-family: "Saira Condensed", "Arial Narrow", sans-serif;
    font-weight: 300;
  }
  .brand-name {
    position: absolute;
    left: 0;
    right: 0;
    top: 140px;
    margin: 0;
    text-align: center;
    font-size: 200px;
    line-height: 1;
    font-weight: 300;
    letter-spacing: 0.1em;
    padding-left: 0.1em;
  }
  .audience-tag {
    position: absolute;
    left: 465px;
    top: 347px;
    width: 268px;
    height: 70px;
    background: var(--accent-plum);
    display: flex;
    align-items: center;
    justify-content: center;
    font-size: 58px;
    font-weight: 300;
    line-height: 1;
    letter-spacing: 0.02em;
  }
  .rule {
    position: absolute;
    left: 189px;
    width: 822px;
    height: 6px;
    background: var(--accent-plum);
  }
  .rule--top { top: 716px; }
  .rule--bottom { top: 857px; }
  .product-name {
    position: absolute;
    left: 0;
    right: 0;
    top: 742px;
    margin: 0;
    text-align: center;
    font-size: 88px;
    font-weight: 300;
    line-height: 1;
    letter-spacing: 0.03em;
  }
  .product-feature {
    position: absolute;
    left: 0;
    right: 0;
    top: 882px;
    margin: 0;
    text-align: center;
    font-size: 58px;
    font-weight: 300;
    line-height: 1;
    letter-spacing: 0.36em;
    padding-left: 0.36em;
  }
</style>
</head>
<body>
  <main class="label">
    <h1 class="brand-name">QUARVINE</h1>
    <div class="audience-tag">FOR ALL</div>
    <div class="rule rule--top"></div>
    <h2 class="product-name">EYE CORRECTOR SERUM</h2>
    <div class="rule rule--bottom"></div>
    <p class="product-feature">WITH TRIPLE PEPTIDES</p>
  </main>
</body>
</html>
```